LASIK low price tagline project

Seeking a creative person to create a catchy tag line, with art, for our LASIK laser vision correction pricing. We wish to lowering our price by half, and keep it that low. The tag line I came up with myself is "Great LASIK value. Low LASIK Price". But it's not too catchy. Also, please know it's illegal to imply surgical results; so, we cannot say something like Great LASIK Outcome at a Low LASIK Price. This campaign would be used in our newsletters and as an online campaign. Our brand standards are attached.

Target Market(s)

Creative designers, wordsmiths, marketing mavens

Industry/Entity Type

Health And Wellness

Font styles to use
Sans Serif

Requirements
Must have
• Short catchy tag line
Nice to have
• illiteration or catchy, memorable phrase
Should not have
• Cannot guarantee a surgical result. Cannot imply a surgical result.

```html
<!DOCTYPE html>
<html lang="en">
<head>
<meta charset="utf-8">
<title>LASIK – High in Value. Low in Price.</title>
<link rel="stylesheet" href="https://fonts.googleapis.com/css2?family=Open+Sans:wght@400;700&display=swap">
<style>
  :root {
    --sky: #96c8da;
    --white: #ffffff;
    --ink: #111111;
  }
  * { margin: 0; padding: 0; box-sizing: border-box; }
  html, body {
    width: 1200px;
    height: 628px;
    overflow: hidden;
    background: var(--sky);
  }
  .ad {
    position: relative;
    width: 1200px;
    height: 628px;
    background: var(--sky);
    font-family: "Open Sans", Arial, sans-serif;
    color: var(--white);
  }
  .headline {
    position: absolute;
    top: 232px;
    left: 0;
    width: 100%;
    text-align: center;
    font-weight: 700;
    font-size: 66px;
    line-height: 1;
    letter-spacing: 0.5px;
  }
  .tagline {
    position: absolute;
    top: 341px;
    left: 0;
    width: 100%;
    text-align: center;
    font-size: 37px;
    line-height: 1;
    font-weight: 400;
    word-spacing: 1px;
  }
  .tagline strong { font-weight: 700; }
  .tagline .gap { display: inline-block; width: 14px; }
  .brand-box {
    position: absolute;
    left: 892px;
    top: 499px;
    width: 280px;
    height: 74px;
    background: var(--white);
    display: flex;
    align-items: center;
    padding: 0 10px 0 6px;
    gap: 10px;
  }
  .brand-mark {
    width: 56px;
    height: 56px;
    background: var(--ink);
    border-radius: 6px;
    flex: none;
  }
  .brand-name {
    font-size: 19px;
    font-weight: 700;
    color: var(--ink);
    white-space: nowrap;
    letter-spacing: -0.3px;
  }
  .web {
    position: absolute;
    right: 30px;
    top: 580px;
    font-size: 18px;
    font-weight: 700;
    color: var(--white);
  }
</style>
</head>
<body>
  <main class="ad">
    <h1 class="headline">LASIK</h1>
    <p class="tagline"><strong>HIGH</strong> IN <strong>VALUE.</strong><span class="gap"></span> <strong>LOW</strong> IN <strong>PRICE.</strong></p>
    <div class="brand-box">
      <span class="brand-mark"></span>
      <span class="brand-name">Clearview Eye Group</span>
    </div>
    <p class="web">www.ClearviewEyeGroup.com</p>
  </main>
</body>
</html>
```